Tallow Creek Stampede Sponsor Brochure/letter

We are wanting a professional looking brochure/letter that can be given to potential sponsors. This can be multiple pages the last page needs to be the Invoice (attached example) the prices on the example can be used.. this is a first nation rodeo and we are looking for sponsorship I can provide more photos if needed

Target Market(s)

This will be local corporate business's so this needs to be very professional looking

Industry/Entity Type

This is an event but we are looking for cooperate sponsorship

Font styles to use
Serif

Colors
0054AA
0677BA
7BADD7
CADEEF
E8F1F8
FFC000
F8CF3A
FAE287
FDF2CF
FEFAEE
F0912C
F2A743
F7CA91
FBE8D2
FDF5EE
EB3D1F
EC4F4E
F09395
F8D3D4
FCEDEE

Requirements
Must have
• The basic information, must have some quotes and photos can be multiple pages
Nice to have
• I would like to see that it is interactive, but gets to the point
Should not have
• no cartoon or must not look cheap

```html
<!DOCTYPE html>
<html lang="en">
<head>
<meta charset="utf-8">
<title>Invoice – Tallow Creek Stampede</title>
<link href="https://fonts.googleapis.com/css2?family=Merriweather:wght@400;700;900&display=swap" rel="stylesheet">
<style>
  :root{
    --blue:#0054AA;
    --orange:#F0912C;
    --band:#CADEEF;
    --pale:#E8F1F8;
    --white:#FFFFFF;
  }
  *{margin:0;padding:0;box-sizing:border-box}
  html,body{width:1020px;height:1200px;overflow:hidden;background:var(--blue)}
  body{font-family:"Merriweather",Georgia,serif;color:var(--white)}
  .invoice{position:relative;width:1020px;height:1200px;background:var(--blue);overflow:hidden}
  .corner-shapes{position:absolute;inset:0}
  .title{position:absolute;right:58px;top:58px;font-weight:900;font-size:48px;letter-spacing:1px;color:var(--white)}
  .field-label{position:absolute;left:91px;font-weight:700;font-size:21px;color:var(--pale)}
  .field-line{position:absolute;left:272px;width:389px;height:1px;background:var(--pale)}

  .line-items{position:absolute;left:89px;top:422px;width:842px}
  .row{display:grid;grid-template-columns:359px 161px 160px 162px;height:36px;border-bottom:1px solid var(--pale)}
  .row > span{display:flex;align-items:center;padding-left:13px;font-size:18px;font-weight:400;color:var(--pale)}
  .row > span + span{border-left:1px solid var(--pale)}
  .row.head{background:var(--orange);border-bottom:none}
  .row.head > span{justify-content:center;padding-left:0;font-weight:700;font-size:18px;color:var(--pale)}
  .row.head > span + span{border-left:1px solid var(--band)}
  .section-band{height:37px;background:var(--band);display:flex;align-items:center;padding-left:13px;font-weight:700;font-size:18px;color:var(--blue)}
  .gap-top{border-top:1px solid var(--pale);margin-top:15px}
  .gap{height:15px}

  .payment{position:absolute;left:89px;top:935px;width:842px;height:85px;background:var(--band);color:var(--blue);font-weight:700;font-size:18.5px}
  .payment .cheque{position:absolute;left:13px;top:7px;line-height:24px}
  .payment .total{position:absolute;left:543px;top:31px}

  .contact{position:absolute;right:376px;text-align:right;font-weight:700;font-size:15.5px;color:var(--pale)}
  .contact-icon{position:absolute;left:656px;width:20px;height:22px}
  .divider{position:absolute;left:711px;top:1043px;width:5px;height:137px;background:var(--band)}
  .nation-mark{position:absolute;left:743px;top:1058px;width:234px;height:118px;display:flex;align-items:center;gap:12px}
  .nation-mark .dot{flex:0 0 44px;height:44px;border-radius:50%;background:var(--band)}
  .nation-mark .name{font-weight:700;font-size:20px;line-height:25px;color:var(--band)}
</style>
</head>
<body>
<main class="invoice">
  <svg class="corner-shapes" width="1020" height="1200" viewBox="0 0 1020 1200" aria-hidden="true">
    <polygon points="0,0 192,0 0,198" fill="var(--orange)"/>
    <polygon points="354,0 1020,0 1020,314" fill="var(--orange)"/>
  </svg>

  <h1 class="title">INVOICE</h1>

  <div class="field-label" style="top:162px">Company Name</div>
  <div class="field-line" style="top:185px"></div>
  <div class="field-label" style="top:203px">Attention</div>
  <div class="field-line" style="top:228px"></div>
  <div class="field-label" style="top:243px">Address</div>
  <div class="field-line" style="top:268px"></div>
  <div class="field-line" style="top:303px"></div>
  <div class="field-label" style="top:312px">Phone Number</div>
  <div class="field-line" style="top:341px"></div>
  <div class="field-label" style="top:356px">Date</div>
  <div class="field-line" style="top:379px"></div>

  <section class="line-items">
    <div class="row head"><span></span><span>QUANTITY</span><span>COST</span><span>TOTAL</span></div>
    <div class="section-band">RODEO PACKAGES</div>
    <div class="row"><span>Starter Package</span><span></span><span></span><span></span></div>
    <div class="row"><span>Bronze Package</span><span></span><span></span><span></span></div>
    <div class="row"><span>Silver Package</span><span></span><span></span><span></span></div>
    <div class="row"><span>Gold Package</span><span></span><span></span><span></span></div>
    <div class="row"><span>Platinum Package</span><span></span><span></span><span></span></div>
    <div class="row gap-top"><span>Take Out</span><span></span><span></span><span></span></div>
    <div class="gap"></div>
    <div class="section-band">EVENT PACKAGES</div>
    <div class="row"><span>Fun Package</span><span></span><span></span><span></span></div>
    <div class="row"><span>Dance Saloon Package</span><span></span><span></span><span></span></div>
    <div class="row"><span>Steak Dinner Package</span><span></span><span></span><span></span></div>
    <div class="row"><span>Pancake Breakfast Package</span><span></span><span></span><span></span></div>
  </section>

  <section class="payment">
    <div class="cheque">Paid by Cheque #<br>Tallow Creek First Nation<br>Memo: Rodeo</div>
    <div class="total">Total Invoice</div>
  </section>

  <div class="contact" style="top:1071px">Tallow Creek First Nation, P.O. Box 18, Aspen Flats, BC V0X 1K0</div>
  <svg class="contact-icon" style="top:1068px" viewBox="0 0 20 22" aria-hidden="true">
    <path d="M10 1a6.5 6.5 0 0 0-6.5 6.5C3.5 12 10 18 10 18s6.5-6 6.5-10.5A6.5 6.5 0 0 0 10 1z" fill="none" stroke="var(--pale)" stroke-width="2"/>
    <circle cx="10" cy="7.5" r="2.4" fill="var(--pale)"/>
    <ellipse cx="10" cy="19.5" rx="7" ry="1.8" fill="none" stroke="var(--pale)" stroke-width="1.4"/>
  </svg>
  <div class="contact" style="top:1102px">250.555.0142</div>
  <svg class="contact-icon" style="top:1100px" viewBox="0 0 20 22" aria-hidden="true">
    <path d="M4 3l3 0 1.5 4-2 1.5c1 2.5 3 4.5 5.5 5.5L13.5 12l4 1.5 0 3C17.5 18 16 19 14.5 19 8 18.5 2.5 13 2 6.5 2 5 3 3 4 3z" fill="none" stroke="var(--pale)" stroke-width="1.8"/>
    <path d="M12 2a7 7 0 0 1 7 7M12 5a4 4 0 0 1 4 4" fill="none" stroke="var(--pale)" stroke-width="1.5"/>
  </svg>
  <div class="contact" style="top:1134px">events@tallowcreekfn.org</div>
  <svg class="contact-icon" style="top:1134px" viewBox="0 0 20 22" aria-hidden="true">
    <rect x="1" y="8" width="18" height="13" fill="none" stroke="var(--pale)" stroke-width="1.8"/>
    <path d="M1 8l9 7 9-7M1 21l7-6M19 21l-7-6" fill="none" stroke="var(--pale)" stroke-width="1.5"/>
    <circle cx="10" cy="5" r="3.5" fill="none" stroke="var(--pale)" stroke-width="1.4"/>
  </svg>

  <div class="divider"></div>
  <div class="nation-mark">
    <span class="dot"></span>
    <span class="name">Tallow Creek<br>First Nation</span>
  </div>
</main>
</body>
</html>
```